Website Redesign for a faith-based, not-for-profit health and human services organization

New website design for the Hearthside Faith Outreach House.
- Current site: www.hfohtr.org -
We are looking for a nice clean, simple, friendly-yet-elegant website layout.
Colors are #f5eed5 (cream), #FFFFFF (white), and all logo colors.
Design a layout for home page
Design a layout for general layouts
-layout only no html needed (preferably a high res PSD file format) -
Main menu should be along top with side navigation for submenu, no side menu on home page.
Also would be open to seeing some updated colors on the logo design, currently the colors are slightly outdated. The Vine of Plenty quilt design fits the organization’s mission and the rural farming / Amish-Mennonite-Brethren community around us.

ADDITIONAL PAGES AND MENU STRUCTURE ON NEW SITE

- How to Help
... Volunteer
... Donate Time
... Donate Money
... Donate Supplies
... Current Needs

- Programs

- News & Events
... Upcoming Events
... Upcoming Fundraisers
... Newsletter

- Our Partners

- About Us
... Overview
... Mission
... Staff Directory
... Board of Directors
... Annual Reports

- Contact

Our annual special event is Gather at the Hearth and should be integrated into the home page - see attached logos and banner

Websites with elements we like (from organizations doing similar work), each for a different reason....

1. http://www.kinbridgeway.org
Good design, color, clarity on this site. Multi-dimensional, photos...easy interaction, etc.

2. http://endfamineplainly.org
Quite simple, nothing fancy, but some good basic stuff here, and pretty easy to navigate...

3. http://www.neighborhub.org
Intrigued by the bulletin board design and the way they have their programs broken down to show impact, needs, etc. It has a lot of good information, but is really too verbose, some of the print is too small, etc. Not perfect, but some interesting design elements.

4. http://sharedlarder.org
Site is boring and not very well designed, but it has some of the features that we would like to see at the top, donations, partners, etc.

5. http://www.meadowlarkgrocers.org
Too many listings on the sidebar - needs to be cleaner & simpler, but a lot of good information and we like the way they show volunteer photos on the Our Helpers Shine Bright page...

About
Hearthside Faith Outreach House ("HFOH" or “the Center”) is a faith-based non-for-profit health and human services organization that exists as an outreach of and for the Ostrel Valley Unified School District.
Tagline: Mercy at Work (we work to serve the needs of the ‘least of these’ with compassion).

Mission
Our mission is to see lives transformed and the community enhanced by encouraging the oppressed, defending the cause of the weak and maintaining the rights of the poor - bringing together the resources of a caring community as a demonstration of the good news of Christ.

Company Overview
Hearthside Faith Outreach House works closely with the community in which it serves. A tremendous value is placed upon the partnerships that have formed with caring people within the community and with organizations that share the goal of bringing together resources to help those who need it most. Individuals, volunteers, churches, corporations, foundations, and government sources all pull together to help make our mission possible.

Since 1996 the Hearthside Faith Outreach House has collaboratively worked to see our community enhanced, adapting programs and services to meet the changing needs of the community.

Target Market(s)

people needing assistance in local community

Industry/Entity Type

Government

Requirements
Must have
• Good social button integration
Should not have
• No Find Us page like old website it is not needed

```html
<!DOCTYPE html>
<html lang="en">
<head>
<meta charset="utf-8">
<title>Hearthside Faith Outreach House</title>
<link rel="stylesheet" href="https://fonts.googleapis.com/css2?family=Ubuntu:wght@400;500;700&display=swap">
<style>
:root{
  --cream:#f5eed5;
  --maroon:#8c1d2c;
  --maroon-dark:#6e1220;
  --maroon-light:#b0303f;
  --gold:#dcb447;
  --charcoal:#333333;
  --charcoal-dark:#2a2a2a;
  --text:#4a4a4a;
  --muted:#8a8a8a;
  --white:#ffffff;
}
*{margin:0;padding:0;box-sizing:border-box}
html,body{width:874px;height:1200px;overflow:hidden;background:var(--cream)}
body{font-family:'Ubuntu',sans-serif;color:var(--text)}
.page{position:relative;width:1020px;height:1400px;transform:scale(0.85686);transform-origin:0 0;background:var(--cream)}
.abs{position:absolute}

.brand{left:22px;top:20px;display:flex;align-items:center;gap:14px}
.brand-mark{width:86px;height:86px;background:var(--maroon)}
.brand-name{color:var(--maroon);font-size:21px;line-height:23px;font-weight:400;width:135px}
.tagline{left:330px;top:62px;font-size:28px;color:var(--maroon);font-weight:400}
.social{left:856px;top:28px;display:flex;align-items:center;gap:6px}
.social span{font-size:9px;font-weight:700;color:#555;letter-spacing:.5px;margin-right:4px}
.social i{display:block;width:28px;height:28px;border-radius:4px;background:#3b5a98}
.social i.second{background:#3aa9e0}

.main-nav{left:32px;top:136px;width:958px;height:30px;border-radius:15px;background:linear-gradient(#b32638,var(--maroon-dark));display:flex;box-shadow:0 1px 2px rgba(0,0,0,.3)}
.main-nav a{color:var(--white);text-decoration:none;font-size:13px;font-weight:500;display:flex;align-items:center;justify-content:center;border-right:1px solid rgba(0,0,0,.25)}
.main-nav a:last-child{border-right:0}

.hero{left:36px;top:188px;width:710px;height:330px;background:var(--maroon);padding:12px;box-shadow:inset 0 0 0 2px #5a0f18}
.hero-photo{width:100%;height:100%;background:linear-gradient(135deg,#9a7a55,#c9a77a 45%,#7a5a3c);box-shadow:0 0 6px rgba(0,0,0,.6)}

.newsletter{left:767px;top:188px;width:222px;height:239px;background:var(--charcoal);border:1px solid #1e1e1e}
.newsletter-head{height:72px;border-bottom:1px solid #222;text-align:center;color:var(--gold);padding-top:12px;background:var(--charcoal-dark)}
.newsletter-head small{display:block;font-size:17px;letter-spacing:.5px}
.newsletter-head strong{display:block;font-size:29px;font-weight:400;line-height:28px}
.field{margin-left:30px;margin-top:8px}
.field label{font-size:11px;color:#aaa;display:block;margin-bottom:4px}
.field div{width:160px;height:21px;background:var(--white)}
.signup-btn{margin:20px auto 0;width:90px;height:30px;background:var(--gold);color:#222;font-size:12px;font-weight:700;display:flex;align-items:center;justify-content:center}

.donate{left:767px;top:446px;width:223px;height:51px;background:linear-gradient(#e6c257,var(--gold));border-radius:4px;box-shadow:0 2px 2px rgba(0,0,0,.3);color:#222;font-weight:700;font-size:15px;display:flex;align-items:center;justify-content:center}
.address{left:767px;top:518px;width:223px;height:167px;background:var(--gold);border-radius:4px;box-shadow:0 2px 2px rgba(0,0,0,.3);color:#222;font-size:12.5px;font-weight:500;line-height:20px;text-align:center;padding-top:22px}

.featured-title{left:35px;top:538px;font-size:28px;color:var(--maroon);font-weight:400}
.featured-copy{left:36px;top:588px;width:670px;font-size:13px;line-height:18px;color:var(--text)}
.pill{display:inline-flex;align-items:center;justify-content:center;height:24px;border-radius:12px;background:linear-gradient(var(--maroon-light),var(--maroon-dark));color:var(--white);font-size:12px;font-weight:700}
.featured-more{left:34px;top:664px;width:130px}

.panel-head{top:722px;width:310px;height:40px;background:linear-gradient(#a8273a,var(--maroon-dark));color:var(--white);font-size:13px;font-weight:700;padding:14px 0 0 24px}
.panel-body{top:762px;width:300px;height:299px;border:1px solid #c9a08a;border-top:0;background:radial-gradient(ellipse at center,#fbf7ea,#f1e7cd)}
.item{position:absolute;left:29px;display:flex;gap:17px}
.thumb{width:70px;height:60px;background:linear-gradient(135deg,#8f7d6a,#d8ccb9 60%,#6d5e4f)}
.item h3{font-size:14.5px;color:var(--maroon);font-weight:700;margin-top:-3px}
.item time{display:block;font-size:10px;color:var(--muted);margin:2px 0 3px}
.item p{font-size:12px;line-height:15px;color:var(--text);width:155px}
.item p b{color:var(--maroon);margin-left:4px}

.event-name{position:absolute;left:0;top:80px;width:100%;text-align:center;color:var(--maroon);font-weight:700;font-size:24px}
.event-note{position:absolute;left:32px;top:150px;width:240px;font-size:12px;line-height:18px;font-weight:700;color:var(--maroon);text-transform:uppercase}
.event-more{position:absolute;left:27px;top:242px;width:130px}

.footer{left:0;top:1098px;width:1020px;height:140px;background:var(--charcoal)}
.footer-links{position:absolute;left:31px;top:23px;font-size:12.5px;color:#ddd}
.footer-links span{margin:0 7px;color:#aaa}
.partner{position:absolute;top:20px;height:60px;background:#e8e8e8;border:2px solid #111}
.footer-rule{position:absolute;left:0;top:99px;width:100%;border-top:1px solid #222}
.footer-legal{position:absolute;left:32px;top:110px;font-size:12.5px;color:#ccc;white-space:nowrap}
.footer-legal span{margin:0 6px}
.bottom-band{left:0;top:1378px;width:1020px;height:22px;background:var(--white)}
</style>
</head>
<body>
<div class="page">
  <header>
    <div class="abs brand"><div class="brand-mark"></div><div class="brand-name">Hearthside Faith Outreach House</div></div>
    <div class="abs tagline">Mercy at Work Since 1996</div>
    <div class="abs social"><span>FOLLOW US</span><i aria-label="Social page"></i><i class="second" aria-label="Social feed"></i></div>
    <nav class="abs main-nav">
      <a style="width:119px">Home</a><a style="width:144px">How to Help</a><a style="width:129px">Programs</a><a style="width:162px">News &amp; Events</a><a style="width:151px">Our Partners</a><a style="width:125px">About Us</a><a style="width:128px">Contact</a>
    </nav>
  </header>

  <div class="abs hero"><div class="hero-photo" role="img" aria-label="Volunteers in aprons serving plates of food at a community meal"></div></div>

  <aside>
    <div class="abs newsletter">
      <div class="newsletter-head"><small>NEWSLETTER</small><strong>SIGNUP</strong></div>
      <div class="field"><label>Name</label><div></div></div>
      <div class="field" style="margin-top:10px"><label>Email</label><div></div></div>
      <div class="signup-btn">SIGN UP</div>
    </div>
    <div class="abs donate">DONATE</div>
    <div class="abs address">Hearthside Faith<br>Outreach House<br>82 North Elmcrest Lane<br>Ostrelburg&nbsp;&nbsp;IN&nbsp;&nbsp;46071<br>Ph.:&nbsp;&nbsp;555.204.3318<br>Fax: 555.204.3390</div>
  </aside>

  <h2 class="abs featured-title">Featured Article</h2>
  <p class="abs featured-copy">Nominati definiebas percipitur at vis. Ferri atqui vim ex, ex adhuc oratio mea. Consul alterum urbanitas an vix. Ex mundi inimicus pri, quo ne quis magna. Usu erant congue te, eum labores blandit eu. Qui nullam admodum petentium cu, quas moderatius dissentiunt vel at, fugit graeci voluptaria per no.</p>
  <span class="abs pill featured-more">Read more</span>

  <div class="abs panel-head" style="left:29px">UPCOMING EVENTS</div>
  <div class="abs panel-body" style="left:34px">
    <div class="item" style="top:30px"><div class="thumb" role="img" aria-label="Volunteers group photo"></div><div><h3>Title Goes Here</h3><time>25 Feb 2013</time><p>Nominati definiebas rebus percipitur vis. <b>Read more</b></p></div></div>
    <div class="item" style="top:119px"><div class="thumb" role="img" aria-label="Child holding a sign"></div><div><h3>Title Goes Here</h3><time>25 Feb 2013</time><p>Nominati definiebas rebus percipitur vis. <b>Read more</b></p></div></div>
    <div class="item" style="top:208px"><div class="thumb" role="img" aria-label="Two staff members"></div><div><h3>Title Goes Here</h3><time>25 Feb 2013</time><p>Nominati definiebas rebus percipitur vis. <b>Read more</b></p></div></div>
  </div>

  <div class="abs panel-head" style="left:354px">FEATURED EVENT</div>
  <div class="abs panel-body" style="left:359px">
    <div class="event-name">Gather at the Hearth</div>
    <p class="event-note">Thank you to Brindle Oak and everyone who helped make our first farm-to-table event a success!</p>
    <span class="pill event-more">Read more</span>
  </div>

  <div class="abs panel-head" style="left:680px">CURRENT NEEDS</div>
  <div class="abs panel-body" style="left:685px">
    <div class="item" style="top:30px"><div class="thumb" role="img" aria-label="Volunteers group photo"></div><div><h3>Title Goes Here</h3><time>25 Feb 2013</time><p>Nominati definiebas rebus percipitur vis. <b>Read more</b></p></div></div>
    <div class="item" style="top:119px"><div class="thumb" role="img" aria-label="Child holding a sign"></div><div><h3>Title Goes Here</h3><time>25 Feb 2013</time><p>Nominati definiebas rebus percipitur vis. <b>Read more</b></p></div></div>
    <div class="item" style="top:208px"><div class="thumb" role="img" aria-label="Two staff members"></div><div><h3>Title Goes Here</h3><time>25 Feb 2013</time><p>Nominati definiebas rebus percipitur vis. <b>Read more</b></p></div></div>
  </div>

  <footer class="abs footer">
    <div class="footer-links">Home<span>|</span>How to Help<span>|</span>Programs<span>|</span>News &amp; Events<span>|</span>Our Partners<span>|</span>About Us<span>|</span>Contact</div>
    <div class="partner" style="left:670px;width:143px" aria-label="Partner badge"></div>
    <div class="partner" style="left:833px;width:157px" aria-label="Partner badge"></div>
    <div class="footer-rule"></div>
    <div class="footer-legal">Copyright © Hearthside Faith Outreach House<span>|</span>82 North Elmcrest Lane&nbsp;&nbsp;Ostrelburg&nbsp;&nbsp;IN&nbsp;&nbsp;46071<span>|</span>Ph.: 555.204.3318&nbsp;&nbsp;Fax 555.204.3390<span>|</span>Privacy Policy<span>|</span>Ethics Policy</div>
  </footer>
  <div class="abs bottom-band"></div>
</div>
</body>
</html>
```